Business Card Design Project

Need business card for new non profit organization that includes the attached logo in some form.
with this information
Name: Martin Holloway Pryce
Title: President & Founder
A: P.O. Box 51637, Portland, Oregon, 97209-1637
E: marty@hollowayfoundation.org
E: marty@martypryce.com
P: 1.971.555.0172

```html
<!DOCTYPE html>
<html lang="en">
<head>
<meta charset="utf-8">
<title>Martin Holloway Pryce — Business Card</title>
<link rel="stylesheet" href="https://fonts.googleapis.com/css2?family=Arimo:wght@700&family=Cabin:wght@700&display=swap">
<style>
  :root {
    --gold: #e8a900;
    --navy: #03115f;
    --black: #000000;
    --paper: #fbfbfb;
    --white: #ffffff;
    --tile-top: #ffffff;
    --tile-bottom: #c9d3d8;
  }
  html, body {
    margin: 0;
    padding: 0;
    overflow: hidden;
    background: var(--white);
  }
  .card {
    position: relative;
    width: 1200px;
    height: 686px;
    background: var(--paper);
    overflow: hidden;
    font-family: "Arimo", Arial, sans-serif;
  }
  .card-shapes {
    position: absolute;
    inset: 0;
  }
  .brand {
    position: absolute;
    left: 66px;
    top: 62px;
    display: flex;
    align-items: center;
    gap: 14px;
  }
  .brand-dot {
    width: 46px;
    height: 46px;
    border-radius: 50%;
    background: var(--navy);
  }
  .brand-name {
    font-weight: 700;
    font-size: 26px;
    color: var(--navy);
    line-height: 1.1;
  }
  .identity {
    position: absolute;
    right: 32px;
    top: 32px;
    text-align: right;
    color: var(--gold);
    font-weight: 700;
  }
  .identity-name {
    font-size: 30px;
    line-height: 36px;
    margin: 0;
  }
  .identity-title {
    font-size: 35px;
    line-height: 40px;
    margin: 0;
  }
  .emails {
    position: absolute;
    left: 699px;
    top: 370px;
    color: var(--white);
    font-size: 25px;
    line-height: 60px;
  }
  .email { display: block; }
  .address {
    position: absolute;
    left: 21px;
    top: 536px;
    color: var(--white);
    font-family: "Cabin", Arial, sans-serif;
    font-weight: 700;
    font-size: 26px;
    line-height: 38px;
  }
  .phone {
    position: absolute;
    left: 843px;
    top: 612px;
    color: var(--white);
    font-size: 25px;
    letter-spacing: 5px;
  }
</style>
</head>
<body>
<div class="card">
  <svg class="card-shapes" width="1200" height="686" viewBox="0 0 1200 686" aria-hidden="true">
    <defs>
      <linearGradient id="tile-fill" x1="0" y1="0" x2="0" y2="1">
        <stop offset="0" stop-color="var(--tile-top)"/>
        <stop offset="1" stop-color="var(--tile-bottom)"/>
      </linearGradient>
    </defs>
    <!-- top band -->
    <path d="M0 0 H1200 V26 Q600 18 0 14 Z" fill="var(--black)"/>
    <path d="M0 18 Q600 22 1200 30" stroke="var(--gold)" stroke-width="3" fill="none"/>
    <!-- lower dark field -->
    <rect x="0" y="385" width="1200" height="301" fill="var(--black)"/>
    <line x1="0" y1="386" x2="534" y2="386" stroke="var(--gold)" stroke-width="4"/>
    <!-- navy address panel -->
    <path d="M-4 392 H640 Q752 400 752 520 Q752 643 640 645 H-4 Z" fill="var(--navy)" stroke="var(--gold)" stroke-width="6"/>
    <!-- email strip, laid over the panel's upper curve -->
    <rect x="676" y="356" width="524" height="137" fill="var(--black)"/>
    <line x1="676" y1="494" x2="1200" y2="494" stroke="var(--gold)" stroke-width="2"/>
    <!-- email tile -->
    <rect x="532" y="347" width="150" height="150" rx="20" fill="url(#tile-fill)" stroke="var(--gold)" stroke-width="4"/>
    <rect x="547" y="382" width="120" height="84" rx="10" fill="var(--gold)"/>
    <rect x="559" y="392" width="96" height="64" fill="none" stroke="var(--white)" stroke-width="3"/>
    <path d="M559 392 L655 456 M655 392 L559 456" stroke="var(--white)" stroke-width="3"/>
    <!-- phone tile -->
    <rect x="755" y="584" width="82" height="82" rx="12" fill="url(#tile-fill)" stroke="var(--gold)" stroke-width="3"/>
    <path d="M784 602 q-10 4 -8 24 q3 20 20 28 q6 3 10 -2 l4 -5 q2 -3 -2 -5 l-8 -5 q-3 -2 -5 1 l-3 3 q-8 -5 -10 -17 l4 -2 q3 -1 2 -5 l-2 -10 q-1 -4 -2 -5 z" fill="var(--gold)"/>
  </svg>

  <div class="brand">
    <span class="brand-dot"></span>
    <span class="brand-name">Holloway<br>Foundation</span>
  </div>

  <div class="identity">
    <p class="identity-name">Martin Holloway Pryce</p>
    <p class="identity-title">President &amp; Founder</p>
  </div>

  <div class="emails">
    <span class="email">marty@hollowayfoundation.org</span>
    <span class="email">marty@martypryce.com</span>
  </div>

  <div class="address">Address: P.O. Box 51637, Portland, Oregon,<br>97209-1637</div>

  <div class="phone">1.971.555.0172</div>
</div>
</body>
</html>
```